Mobile Friendly Lead Generation Landing Page

We are a web marketing company that specialized in web lead generation. Recently we have started buying media from mobile devices and we need a mobile interface(landing page) where we can collect user data in an effective manner.

Our current mobile landing page is:
http://www.tuitionscout.example.com/lp13d/index.aspx?a=true&source=581406
Through this you can see what the steps/questions users need to answer to get matched to a school. We need the design for the whole process.

We are pretty open for design ideas and our goal is to make this mobile optimized landing page have the look and feel of an app...but not an app.
There are several questions in the process but we are open to changing the way they are presented. As in, you can have one question at a time or a few.
The goal is to make this EXTREMELY EASY for users to interact with.

One example that we have liked is:
http://lessonhub.example/schools/47215-page1.lhub (please note that this opens only on mobile devices)

Some of these screenshots are attached.

Our web form looks like this:
http://www.tuitionscout.example.com/lp88/index.aspx?a=true

```html
<!DOCTYPE html>
<html lang="en">
<head>
<meta charset="utf-8">
<title>Select Area of Interest</title>
<link rel="stylesheet" href="https://fonts.googleapis.com/css2?family=Arimo:wght@400;700&display=swap">
<style>
  :root {
    --red: #ee1c2e;
    --blue: #0ba2f2;
    --icon-blue: #0aa3f5;
    --olive: #9aa551;
    --olive-line: #7f8a3c;
    --text: #333333;
    --chevron: #7a7a7a;
    --divider: #cfcfcf;
    --white: #ffffff;
    --banner-top: #e6ecf3;
    --banner-mid: #e4dde2;
    --banner-end: #dde5de;
    --foot-a: #e6f3ef;
    --foot-b: #cdeefa;
  }
  * { box-sizing: border-box; margin: 0; padding: 0; }
  html, body { width: 678px; height: 1200px; overflow: hidden; }
  body {
    font-family: "Arimo", "Helvetica Neue", Arial, sans-serif;
    background: var(--white);
    color: var(--text);
  }
  .page { position: relative; width: 678px; height: 1200px; overflow: hidden; }

  .promo {
    position: relative;
    height: 272px;
    background: linear-gradient(100deg, var(--banner-top) 0%, var(--banner-mid) 55%, var(--banner-end) 100%);
  }
  .promo-figure {
    position: absolute;
    left: 22px; top: 26px;
    width: 118px; height: 120px;
    border-radius: 50% 50% 8px 8px;
    background: linear-gradient(180deg, #a8b15e 0%, #9aa551 100%);
    opacity: .85;
  }
  .promo-title {
    position: absolute;
    left: 171px; top: 24px;
    font-size: 41px; font-weight: 400;
    color: var(--red);
    letter-spacing: .2px;
  }
  .promo-title-2 {
    position: absolute;
    right: 31px; top: 76px;
    font-size: 43px; font-weight: 700;
    color: var(--blue);
  }
  .promo-title-2 span { color: var(--red); font-weight: 400; }
  .promo-band {
    position: absolute;
    left: 0; right: 0; top: 146px;
    height: 73px;
    background: var(--olive);
    border-top: 1px solid var(--olive-line);
    border-bottom: 1px solid var(--olive-line);
    color: var(--white);
    font-size: 21px;
    display: flex; align-items: center; justify-content: center;
    letter-spacing: .1px;
  }

  .section-title {
    height: 92px;
    background: var(--red);
    color: var(--white);
    font-size: 31px;
    display: flex; align-items: center; justify-content: center;
  }

  .interest-list { list-style: none; background: var(--white); }
  .interest {
    position: relative;
    height: 93px;
    display: flex; align-items: center;
    padding-left: 29px;
  }
  .interest::after {
    content: "";
    position: absolute;
    left: 32px; right: 0; bottom: 0;
    border-bottom: 1px solid var(--divider);
  }
  .interest:last-child::after { left: 0; border-color: #b9b3a6; }
  .interest-icon {
    width: 64px; height: 64px;
    border-radius: 9px;
    background: var(--icon-blue);
    display: flex; align-items: center; justify-content: center;
    flex-shrink: 0;
  }
  .interest-icon svg { width: 44px; height: 44px; }
  .interest-label { margin-left: 19px; font-size: 27px; color: var(--text); flex: 1; }
  .chevron { width: 16px; height: 26px; margin-right: 34px; }

  .footer-fill {
    height: 186px;
    background: linear-gradient(100deg, var(--foot-a) 0%, var(--foot-b) 100%);
  }
</style>
</head>
<body>
<main class="page">
  <header class="promo">
    <div class="promo-figure" role="img" aria-label="Illustration of a graduate in a cap holding a magnifying glass"></div>
    <h1 class="promo-title">Complete our</h1>
    <p class="promo-title-2">3-minute <span>app!</span></p>
    <p class="promo-band">GET UP TO $5, 645* PER YEAR IN GRANTS IF YOU QUALIFY</p>
  </header>

  <h2 class="section-title">SELECT AREA OF YOUR INTEREST</h2>

  <ul class="interest-list">
    <li class="interest">
      <span class="interest-icon">
        <svg viewBox="0 0 44 44" fill="none" stroke="#fff" stroke-width="1.6" stroke-linecap="round" stroke-linejoin="round">
          <path d="M36 6 L20 24"/><path d="M33 5 L17 22 L22 27 L38 9 Z"/>
          <path d="M17 25 C11 25 11 31 9 36 C15 36 21 34 21 29"/>
        </svg>
      </span>
      <span class="interest-label">Art &amp; Design</span>
      <svg class="chevron" viewBox="0 0 16 26" fill="none" stroke="var(--chevron)" stroke-width="3" stroke-linecap="round"><path d="M3 3 L13 13 L3 23"/></svg>
    </li>
    <li class="interest">
      <span class="interest-icon">
        <svg viewBox="0 0 44 44" fill="none" stroke="#fff" stroke-width="1.6" stroke-linejoin="round">
          <rect x="6" y="13" width="32" height="22" rx="1"/>
          <path d="M17 13 V9 H27 V13"/><path d="M6 21 H38"/><rect x="20" y="19" width="4" height="4"/>
        </svg>
      </span>
      <span class="interest-label">Business</span>
      <svg class="chevron" viewBox="0 0 16 26" fill="none" stroke="var(--chevron)" stroke-width="3" stroke-linecap="round"><path d="M3 3 L13 13 L3 23"/></svg>
    </li>
    <li class="interest">
      <span class="interest-icon">
        <svg viewBox="0 0 44 44" fill="none" stroke="#fff" stroke-width="1.6" stroke-linejoin="round" stroke-linecap="round">
          <rect x="16" y="7" width="10" height="16" rx="1" transform="rotate(45 21 15)"/>
          <path d="M16 21 L6 31 L8 33 L18 23"/><path d="M20 37 H38"/>
        </svg>
      </span>
      <span class="interest-label">Criminal Justice</span>
      <svg class="chevron" viewBox="0 0 16 26" fill="none" stroke="var(--chevron)" stroke-width="3" stroke-linecap="round"><path d="M3 3 L13 13 L3 23"/></svg>
    </li>
    <li class="interest">
      <span class="interest-icon">
        <svg viewBox="0 0 44 44">
          <text x="22" y="18" fill="#fff" font-family="Arimo, sans-serif" font-size="13" text-anchor="middle">ABC</text>
          <line x1="6" y1="22" x2="38" y2="22" stroke="#fff" stroke-width="1.4"/>
          <text x="22" y="36" fill="#fff" font-family="Arimo, sans-serif" font-size="13" text-anchor="middle">1 2 3</text>
        </svg>
      </span>
      <span class="interest-label">Education &amp; Teaching</span>
      <svg class="chevron" viewBox="0 0 16 26" fill="none" stroke="var(--chevron)" stroke-width="3" stroke-linecap="round"><path d="M3 3 L13 13 L3 23"/></svg>
    </li>
    <li class="interest">
      <span class="interest-icon">
        <svg viewBox="0 0 44 44" fill="none" stroke="#fff" stroke-width="1.6" stroke-linecap="round">
          <circle cx="22" cy="9" r="3"/><path d="M22 4 V6"/>
          <path d="M20 12 L10 36"/><path d="M24 12 L34 36"/>
          <path d="M8 28 C16 34 28 34 36 28"/><path d="M6 38 H38"/>
        </svg>
      </span>
      <span class="interest-label">Engineering</span>
      <svg class="chevron" viewBox="0 0 16 26" fill="none" stroke="var(--chevron)" stroke-width="3" stroke-linecap="round"><path d="M3 3 L13 13 L3 23"/></svg>
    </li>
    <li class="interest">
      <span class="interest-icon">
        <svg viewBox="0 0 44 44" fill="none" stroke="#fff" stroke-width="1.6" stroke-linejoin="round">
          <path d="M6 12 C12 9 18 9 22 13 C26 9 32 9 38 12 V34 C32 31 26 31 22 35 C18 31 12 31 6 34 Z"/>
          <path d="M22 13 V35"/>
        </svg>
      </span>
      <span class="interest-label">Other</span>
      <svg class="chevron" viewBox="0 0 16 26" fill="none" stroke="var(--chevron)" stroke-width="3" stroke-linecap="round"><path d="M3 3 L13 13 L3 23"/></svg>
    </li>
  </ul>

  <div class="footer-fill"></div>
</main>
</body>
</html>
```